electrical contractor business card for professional modern company

I need a business card design for an electrical contractors business. I do all kinds of electricical work from new homes, air conditioning, data and communications. I have a logo design i want on it and have a good idea in my head of what i want it to look like. I like simple yet bold and professional looking. All black background is a must

Target Market(s)

Anyone needing electrical work done

Industry/Entity Type

Electrical

Contact Information for Business Card

company name- KTW Electrical and Data
person name-martin pellowe
phone number- 0418 362 927
website-ktwelec.example.com.au

Font styles to use
Sans Serif

Requirements
Must have
• email
• website
• logo
• name
• phone number
• list of work i do:
• -electrical
• -air-conditioning
• -data/communications
• -cctv/security
• -domestic/commercial/industrial
• -24hr emergency breakdown repair
Nice to have
• i would like the logo on the front side in the centre taking up most of the card with black background.
• on the rear i want the list of work i do with company info i.e. email, website, my name, phone number. rear of card also black background with orange writing to match the orange in the logo

```html
<!DOCTYPE html>
<html lang="en">
<head>
<meta charset="utf-8">
<title>KTW Electrical and Data – Business Card</title>
<link href="https://fonts.googleapis.com/css2?family=Open+Sans:wght@300;400;600&display=swap" rel="stylesheet">
<style>
  :root {
    --canvas: #e9e7e4;
    --card: #050505;
    --orange: #f26b1d;
    --orange-faint: rgba(242, 107, 29, 0.18);
    --shadow: rgba(0, 0, 0, 0.28);
  }
  * { box-sizing: border-box; margin: 0; padding: 0; }
  html, body {
    width: 1200px;
    height: 800px;
    overflow: hidden;
    background: var(--canvas);
    font-family: "Open Sans", Arial, sans-serif;
  }
  .stage {
    position: relative;
    width: 1200px;
    height: 800px;
  }
  .card {
    position: absolute;
    background: var(--card);
    box-shadow: 0 10px 30px var(--shadow);
    overflow: hidden;
    color: var(--orange);
  }

  /* Front — portrait card, content set sideways */
  .card-front {
    left: 70px;
    top: 130px;
    width: 340px;
    height: 540px;
  }
  .card-front .front-content {
    position: absolute;
    width: 540px;
    height: 340px;
    left: -100px;
    top: 100px;
    transform: rotate(90deg);
    display: flex;
    flex-direction: column;
    align-items: center;
    justify-content: center;
    gap: 26px;
  }
  .brand-lockup {
    display: flex;
    align-items: center;
    gap: 14px;
  }
  .brand-dot {
    width: 22px;
    height: 22px;
    border-radius: 50%;
    background: var(--orange);
  }
  .brand-name {
    font-weight: 600;
    font-size: 30px;
    letter-spacing: 1px;
    text-transform: uppercase;
    color: var(--orange);
  }
  .front-web {
    font-weight: 400;
    font-size: 22px;
  }

  /* Back — landscape card */
  .card-back {
    left: 470px;
    top: 210px;
    width: 660px;
    height: 400px;
  }
  .back-decoration {
    position: absolute;
    left: 250px;
    top: 90px;
    width: 330px;
    height: 330px;
    border-radius: 50%;
    background: var(--orange-faint);
  }
  .holder-name {
    position: absolute;
    left: 46px;
    top: 38px;
    font-weight: 300;
    font-size: 36px;
  }
  .contact-list {
    position: absolute;
    left: 46px;
    top: 110px;
    list-style: none;
    font-size: 15px;
    line-height: 28px;
  }
  .contact-list li {
    display: flex;
    align-items: center;
    gap: 10px;
  }
  .contact-list svg {
    width: 15px;
    height: 15px;
    fill: var(--orange);
  }
  .card-back .brand-lockup {
    position: absolute;
    left: 330px;
    top: 120px;
    gap: 10px;
  }
  .card-back .brand-name { font-size: 19px; }
  .card-back .brand-dot { width: 16px; height: 16px; }
  .services {
    position: absolute;
    left: 300px;
    top: 200px;
    list-style: none;
    font-size: 16px;
    line-height: 24px;
  }
  .services li::before {
    content: "•";
    margin-right: 10px;
  }
</style>
</head>
<body>
<main class="stage">

  <section class="card card-front" aria-label="Card front">
    <div class="front-content">
      <div class="brand-lockup">
        <span class="brand-dot"></span>
        <span class="brand-name">KTW Electrical and Data</span>
      </div>
      <p class="front-web">ktwelec.example.com.au</p>
    </div>
  </section>

  <section class="card card-back" aria-label="Card back">
    <div class="back-decoration" aria-hidden="true"></div>

    <h1 class="holder-name">Martin Pellowe</h1>

    <ul class="contact-list">
      <li>
        <svg viewBox="0 0 16 16" aria-hidden="true"><path d="M3.6 1.5l2.3 2.6-1.2 1.7c.8 1.9 2.3 3.4 4.1 4.3l1.7-1.2 2.6 2.3-1.3 2.3C6.8 13.5 2.5 9.2 1.4 3.1z"/></svg>
        <span>0418 362 927</span>
      </li>
      <li>
        <svg viewBox="0 0 16 16" aria-hidden="true"><path d="M1 3h14v10H1zM2.5 4.5v.3L8 9l5.5-4.2v-.3zM2.5 6.6v5h11v-5L8 10.8z"/></svg>
        <span>martin@ktwelec.example.com.au</span>
      </li>
      <li>
        <svg viewBox="0 0 16 16" aria-hidden="true"><path d="M8 1a7 7 0 100 14A7 7 0 008 1zm0 1.5c.8 0 1.7 1.5 2 4H6c.3-2.5 1.2-4 2-4zM2.6 7h2c0 .7 0 1.4.1 2h-2a5.6 5.6 0 010-2zm0 3h2.2c.2 1.3.6 2.4 1.1 3.1A5.5 5.5 0 012.6 10zm3.4 0h4c-.3 2.2-1.2 3.5-2 3.5S6.3 12.2 6 10zm0-1c-.1-.6-.1-1.3 0-2h4c.1.7.1 1.4 0 2zm5.2 1h2.2a5.5 5.5 0 01-3.3 3.1c.5-.7.9-1.8 1.1-3.1zm.1-1c.1-.6.1-1.3.1-2h2a5.6 5.6 0 010 2z"/></svg>
        <span>ktwelec.example.com.au</span>
      </li>
    </ul>

    <div class="brand-lockup">
      <span class="brand-dot"></span>
      <span class="brand-name">KTW Electrical and Data</span>
    </div>

    <ul class="services">
      <li>electrical</li>
      <li>air-conditioning</li>
      <li>data/communications</li>
      <li>cctv/security</li>
      <li>domestic/commercial/industrial</li>
      <li>24hr emergency breakdown repair</li>
    </ul>
  </section>

</main>
</body>
</html>
```